Dovenmarch Luxury Landscapes

A landscape business card.

Target Market(s)

Middle aged and up. Professionals.

Industry/Entity Type

Landscape

Contact Information for Business Card

Thornbeck

Colors
0054AA
0677BA
7BADD7
CADEEF
E8F1F8
0094D4
00A9DD
6FCCEA
C7EBF8
E9F6FB

Requirements
Must have
• The color blue and silver be very attractive
Nice to have
• An embossed logo. A watermark of a plant or something that indicates that we are a landscape company in the background of the backside where list of services are offered. . List of services on the back.
Should not have
• Red, yellow, orange.

```html
<!DOCTYPE html>
<html lang="en">
<head>
<meta charset="utf-8">
<title>Dovenmarch Luxury Landscapes – Business Card</title>
<link rel="stylesheet" href="https://fonts.googleapis.com/css2?family=Roboto:wght@400;500;700&display=swap">
<style>
  :root {
    --stage: #3a3a3a;
    --card-white: #ffffff;
    --brand-blue: #2d3fae;
    --back-blue-top: #3550b8;
    --back-blue-bottom: #27399e;
    --text-grey: #5b5b5b;
    --silver: #e4e8f2;
  }
  * { box-sizing: border-box; margin: 0; padding: 0; }
  html, body { width: 1200px; height: 900px; overflow: hidden; }
  body {
    background: var(--stage);
    font-family: "Roboto", Arial, sans-serif;
    position: relative;
  }
  .card {
    position: absolute;
    left: 280px;
    width: 640px;
    height: 366px;
    border-radius: 22px;
    overflow: hidden;
  }
  .card--front { top: 70px; background: var(--card-white); }
  .card--back {
    top: 464px;
    background: linear-gradient(135deg, var(--back-blue-top), var(--back-blue-bottom));
    color: var(--silver);
  }

  /* front */
  .front-brand {
    position: absolute;
    left: 40px; top: 0; width: 250px; height: 100%;
    display: flex; flex-direction: column; justify-content: center; align-items: center;
    text-align: center; color: var(--brand-blue);
  }
  .brand-dot {
    width: 54px; height: 54px; border-radius: 50%;
    border: 3px solid var(--brand-blue); margin-bottom: 14px;
  }
  .brand-name { font-weight: 700; font-size: 26px; line-height: 1.15; letter-spacing: 0.5px; }
  .front-divider {
    position: absolute; left: 310px; top: 58px; width: 2px; height: 250px;
    background: var(--brand-blue);
  }
  .front-details {
    position: absolute; left: 338px; top: 72px; right: 24px;
    color: var(--text-grey);
  }
  .holder-name { color: var(--brand-blue); font-weight: 700; font-size: 30px; }
  .holder-title { font-size: 22px; margin-top: 2px; }
  .address { font-size: 17px; line-height: 1.35; margin-top: 22px; }
  .contact-list { list-style: none; margin-top: 10px; font-size: 17px; line-height: 1.45; }
  .contact-list li { display: flex; align-items: center; gap: 8px; }
  .contact-list svg { width: 15px; height: 15px; flex: none; }

  /* back */
  .services {
    position: absolute; left: 50px; top: 44px; width: 320px;
    font-size: 17px; line-height: 1.55;
  }
  .services-heading { font-weight: 700; font-size: 18px; margin-bottom: 2px; }
  .services-list { list-style: none; }
  .services-list li { white-space: nowrap; }
  .services-list li::before { content: "•"; margin-right: 8px; }
  .back-brand {
    position: absolute; right: 36px; bottom: 34px; width: 220px;
    display: flex; flex-direction: column; align-items: center; text-align: center;
    color: var(--silver);
  }
  .back-brand .brand-dot { border-color: var(--silver); width: 60px; height: 60px; margin-bottom: 10px; }
  .back-brand .brand-name { font-size: 22px; }
</style>
</head>
<body>
  <section class="card card--front">
    <div class="front-brand">
      <div class="brand-dot"></div>
      <div class="brand-name">Dovenmarch Luxury Landscapes</div>
    </div>
    <div class="front-divider"></div>
    <div class="front-details">
      <div class="holder-name">Maren Oakhollow</div>
      <div class="holder-title">Founder &amp; CEO</div>
      <p class="address">18C Fernlow Road, Thornbeck,<br>Nova Scotia, B3K 4P2.</p>
      <ul class="contact-list">
        <li><svg viewBox="0 0 16 16"><path d="M3 1l3 3-1.5 2a9 9 0 0 0 5.5 5.5L12 10l3 3-2 2C7 15 1 9 1 3z" fill="#2d3fae"/></svg>902-555-0187</li>
        <li><svg viewBox="0 0 16 16"><rect x="1" y="3" width="14" height="10" fill="none" stroke="#2d3fae" stroke-width="1.6"/><path d="M1 3l7 6 7-6" fill="none" stroke="#2d3fae" stroke-width="1.6"/></svg>info@dovenmarch.com</li>
        <li><svg viewBox="0 0 16 16"><circle cx="8" cy="8" r="6.5" fill="none" stroke="#2d3fae" stroke-width="1.4"/><ellipse cx="8" cy="8" rx="3" ry="6.5" fill="none" stroke="#2d3fae" stroke-width="1.2"/><path d="M1.5 8h13" stroke="#2d3fae" stroke-width="1.2"/></svg>www.dovenmarch.com</li>
      </ul>
    </div>
  </section>

  <section class="card card--back">
    <div class="services">
      <div class="services-heading">We build:</div>
      <ul class="services-list">
        <li>Decks</li>
        <li>Pools</li>
        <li>Garden Install and Cleanup</li>
        <li>Retaining Walls</li>
        <li>Interlock Stone</li>
        <li>Outdoor Lighting</li>
        <li>Auto Mower Installs and so much more</li>
      </ul>
    </div>
    <div class="back-brand">
      <div class="brand-dot"></div>
      <div class="brand-name">Dovenmarch Luxury Landscapes</div>
    </div>
  </section>
</body>
</html>
```